Car Wrap Design - Korvanteko Weldar Dual Cab Ute

We need a car wrap for a 2018 Korvanteko Weldar Ute - Dual Cab with Canopy. It's Used as a security and medical response vehicle.
Professional Look and finish needed.
Style guide attached.
Must have the words "Security & Medical Response"
Must have brellicanworksgroup.com
Must have phone number at rear 1800 392 816
Must have logo and company name
car image att

Industry/Entity Type

Security, Safety and Medical Response

Other font styles liked:
• Style Guide Att

Requirements
Must have
• Company Name, Website and Phone number. Must have words "Security & Medical Response"

```html
<!DOCTYPE html>
<html lang="en">
<head>
<meta charset="utf-8">
<title>Brellican Works – Korvanteko Weldar Wrap Layouts</title>
<link rel="stylesheet" href="https://fonts.googleapis.com/css2?family=Poppins:wght@500;700&family=Oswald:wght@500&display=swap">
<style>
  :root {
    --canvas: #ffffff;
    --body-white: #f3f4f4;
    --body-line: #c9cccc;
    --glass: #3a3f42;
    --wrap-green: #3a9b4b;
    --wrap-black: #1f1f1f;
    --ink: #232323;
    --band-text: #ffffff;
  }
  html, body {
    margin: 0;
    padding: 0;
    width: 1200px;
    height: 1200px;
    overflow: hidden;
    background: var(--canvas);
  }
  .wrap-sheet { display: block; width: 1200px; height: 1200px; }
  .vehicle-body { fill: var(--body-white); stroke: var(--body-line); stroke-width: 1.5; }
  .glass { fill: var(--glass); }
  .green { fill: var(--wrap-green); }
  .black { fill: var(--wrap-black); }
  .brand-name {
    font-family: "Poppins", sans-serif;
    font-weight: 700;
    fill: var(--ink);
  }
  .brand-name--main { font-size: 46px; letter-spacing: -0.5px; }
  .brand-name--sub { font-size: 27px; letter-spacing: 5px; }
  .tagline {
    font-family: "Oswald", sans-serif;
    font-weight: 500;
    font-size: 13px;
    letter-spacing: 3px;
    fill: var(--band-text);
  }
  .phone {
    font-family: "Poppins", sans-serif;
    font-weight: 700;
    font-size: 21px;
    letter-spacing: 1px;
    fill: var(--ink);
  }
  .website {
    font-family: "Poppins", sans-serif;
    font-weight: 500;
    font-size: 15px;
    fill: var(--ink);
  }
</style>
</head>
<body>
<svg class="wrap-sheet" viewBox="0 0 960 960" xmlns="http://www.w3.org/2000/svg">
  <defs>
    <path id="ute-profile" d="M22,265 L60,235 L235,205 L300,135 L610,130 L625,118 L910,115 L925,140 L935,330 L760,350 A82,82 0 0 0 600,352 L230,355 A80,80 0 0 0 80,345 L30,340 Z"/>
    <clipPath id="ute-clip"><use href="#ute-profile"/></clipPath>
  </defs>

  <!-- Layout option A: diagonal stripe -->
  <g class="layout layout--stripe">
    <use href="#ute-profile" class="vehicle-body"/>
    <g clip-path="url(#ute-clip)">
      <polygon class="green" points="40,268 640,188 640,196 40,278"/>
      <polygon class="green" points="560,360 940,270 940,360"/>
      <polygon class="black" points="225,336 940,250 940,274 225,360"/>
      <text class="tagline" transform="translate(282,350) rotate(-6.9)">SECURITY &amp; MEDICAL RESPONSE</text>
    </g>
    <path class="glass" d="M245,210 L305,145 L435,143 L435,215 Z"/>
    <path class="glass" d="M445,143 L590,143 L595,200 L445,213 Z"/>
    <rect class="glass" x="635" y="130" width="240" height="63" rx="8"/>
    <rect class="green" x="232" y="250" width="52" height="52"/>
    <text class="brand-name brand-name--main" x="298" y="275">BRELLICAN</text>
    <text class="brand-name brand-name--sub" x="302" y="305">WORKS</text>
    <text class="phone" x="645" y="234">1800 392 816</text>
    <text class="website" x="645" y="254">brellicanworksgroup.com</text>
  </g>

  <!-- Layout option B: rear green panel -->
  <g class="layout layout--panel" transform="translate(0,435)">
    <use href="#ute-profile" class="vehicle-body"/>
    <g clip-path="url(#ute-clip)">
      <polygon class="green" points="545,362 650,110 960,110 960,420 545,420"/>
      <polygon class="black" points="618,180 646,112 662,112 634,180"/>
      <polygon class="black" points="815,420 900,205 960,205 960,420"/>
      <rect class="black" x="225" y="333" width="330" height="24"/>
      <text class="tagline" x="270" y="350">SECURITY &amp; MEDICAL RESPONSE</text>
    </g>
    <path class="glass" d="M245,210 L305,145 L435,143 L435,215 Z"/>
    <path class="glass" d="M445,143 L590,143 L595,200 L445,213 Z"/>
    <rect class="glass" x="660" y="130" width="215" height="63" rx="8"/>
    <rect class="green" x="232" y="250" width="52" height="52"/>
    <text class="brand-name brand-name--main" x="298" y="275">BRELLICAN</text>
    <text class="brand-name brand-name--sub" x="302" y="305">WORKS</text>
    <text class="phone" x="652" y="234">1800 392 816</text>
    <text class="website" x="652" y="254">brellicanworksgroup.com</text>
  </g>
</svg>
</body>
</html>
```